Tavelin Global Kft. is an online recruitment marketplace connecting the employers and recruiters together. We provide an e-bussiness solution for companies and give busines opportunity for recruiters.
We have a logo design already, which should be used on the business card.
Our colours are grey and magenta, which can be seen in the logo. Black is also welcome.
The style should be dynamic, young but professional. It should be clear, visible, elegant, not too crowded, simple but exciting.
We need the following data on the BC: name, title, address, phone,fax and mobile number, email address, website.
Target Market(s)
Our target market are companies, as this is a B2B business. We also target recruiters, recruitment professionals, headhunters.We would like to be impressive and different.
Industry/Entity Type
Business
Requirements
Must have
- We would like to promote our website, www.tavelglob.hu.
- Please, put this on the back with a quite visible letter size.The style should be dynamic, young but professional. It should be clear, visible, elegant, not too crowded, simple but exciting.
Should not have
- We do not want to see people figures.

```html
<!DOCTYPE html>
<html lang="en">
<head>
<meta charset="utf-8">
<title>Tavelin Global Kft. – Business Card</title>
<link rel="stylesheet" href="https://fonts.googleapis.com/css2?family=Arimo:ital,wght@0,400;0,700;1,700&display=swap">
<style>
  :root {
    --magenta: #d4137a;
    --magenta-deep: #b50d66;
    --grey: #8a8388;
    --black: #0b0b0b;
    --white: #ffffff;
    --white-soft: rgba(255,255,255,.85);
    --backdrop: #1c1c1e;
  }
  * { margin: 0; padding: 0; box-sizing: border-box; }
  html, body { width: 1200px; height: 900px; overflow: hidden; }
  body {
    background: var(--backdrop);
    font-family: "Arimo", Arial, sans-serif;
    position: relative;
  }
  .card {
    position: absolute;
    width: 560px;
    height: 340px;
    border-radius: 4px;
    overflow: hidden;
    box-shadow: 0 14px 40px rgba(0,0,0,.55);
  }

  /* Front */
  .card-front {
    left: 110px;
    top: 90px;
    background:
      radial-gradient(ellipse 62% 48% at 52% 44%, var(--white) 0%, rgba(255,255,255,.92) 35%, rgba(255,255,255,0) 100%),
      var(--magenta);
  }
  .card-front .brand {
    position: absolute;
    left: 0; right: 0; top: 110px;
    display: flex;
    align-items: center;
    justify-content: center;
    gap: 16px;
  }
  .brand-mark {
    width: 44px; height: 44px;
    background: var(--magenta);
  }
  .brand-name {
    font-weight: 700;
    font-size: 46px;
    color: var(--magenta-deep);
    letter-spacing: .5px;
  }
  .website {
    position: absolute;
    left: 0; right: 0; bottom: 36px;
    text-align: center;
    font-weight: 700;
    font-style: italic;
    font-size: 30px;
    color: var(--white);
  }

  /* Back */
  .card-back {
    left: 530px;
    top: 450px;
    background: var(--magenta);
  }
  .corner-block {
    position: absolute;
    left: 0; top: 0;
    width: 150px; height: 120px;
    background: var(--black);
  }
  .card-back .brand {
    position: absolute;
    right: 26px; top: 22px;
    display: flex;
    align-items: center;
    gap: 8px;
  }
  .card-back .brand-mark {
    width: 22px; height: 22px;
    background: var(--grey);
  }
  .card-back .brand-name {
    font-size: 22px;
    color: var(--grey);
  }
  .identity {
    position: absolute;
    right: 60px; top: 112px;
    text-align: right;
    color: var(--white);
  }
  .person-name {
    font-size: 30px;
    font-weight: 400;
  }
  .job-title {
    margin-top: 6px;
    font-size: 15px;
    color: var(--white-soft);
  }
  .contact {
    position: absolute;
    left: 30px; right: 26px; bottom: 24px;
    display: grid;
    grid-template-columns: 1fr 1fr;
    row-gap: 7px;
    font-size: 14px;
    color: var(--white);
  }
  .contact .right { text-align: right; }
</style>
</head>
<body>
  <section class="card card-front" aria-label="Business card front">
    <div class="brand">
      <span class="brand-mark"></span>
      <span class="brand-name">Tavelin Global</span>
    </div>
    <p class="website">www.tavelglob.hu</p>
  </section>

  <section class="card card-back" aria-label="Business card back">
    <div class="corner-block"></div>
    <div class="brand">
      <span class="brand-mark"></span>
      <span class="brand-name">Tavelin Global</span>
    </div>
    <div class="identity">
      <h1 class="person-name">Marcus Hollen</h1>
      <p class="job-title">Business Development Manager</p>
    </div>
    <div class="contact">
      <span class="address">1052 Budapest, Petőfi u. 14.</span>
      <span class="fax right">fax: +36 1 555 0143</span>
      <span class="phone">phone: +36 1 555 0142</span>
      <span class="mobile right">mobile: +36 30 555 0187</span>
      <span class="web">www.tavelglob.hu</span>
      <span class="email right">e-mail: m.hollen@tavelglob.hu</span>
    </div>
  </section>
</body>
</html>
```